KORVEN Design

We have a 5 part framework that companies use to plot their social media strategies and digital transformation activity. We would like to display the 5 elements in a circular format (please see the attachment for our current design - we want to get a better version of that).

The five elements and their meaning can be read about here: http://plumvexstudio.example/korven/about-korven/
We would like to see designs that fit our corporate image but also maintain informality and simplicity…. Ive included another image of some of the icons we've been using and enjoying to give an understanding of the stuff we like

Target Market(s)

Corporates

Industry/Entity Type

Digital

Logo Text

Brokerage, Integration, Trust, Incentives, Leadership

Colors
0255a3

Requirements
Must have
• Must be circular in format with each element neatly labelled - PLEASE REVIEW OUR CURRENT VERSION IN THE ATTACHMENTS

```html
<!DOCTYPE html>
<html lang="en">
<head>
<meta charset="utf-8">
<title>KORVEN Framework</title>
<link rel="stylesheet" href="https://fonts.googleapis.com/css2?family=Source+Sans+3:wght@400;600&display=swap">
<style>
  :root {
    --brand-blue: #0a55a3;
    --tint-light: #eef4fb;
    --tint-mid: #a9c3e2;
    --tint-deep: #5d8cc4;
    --paper: #ffffff;
  }
  html, body {
    margin: 0;
    padding: 0;
    width: 1200px;
    height: 1000px;
    overflow: hidden;
    background: var(--paper);
  }
  .framework {
    display: block;
    width: 1200px;
    height: 1000px;
    font-family: "Source Sans 3", "Myriad Pro", sans-serif;
  }
  .orbit-ring {
    fill: none;
    stroke: var(--brand-blue);
    stroke-width: 10;
  }
  .element-badge {
    fill: var(--paper);
    stroke: var(--brand-blue);
    stroke-width: 11;
  }
  .element-badge-inner {
    fill: none;
    stroke: var(--brand-blue);
    stroke-width: 1.5;
  }
  .element-icon {
    fill: url(#icon-tone);
  }
  .chart-bar {
    fill: var(--paper);
    stroke: var(--brand-blue);
    stroke-width: 2.5;
  }
  .chart-arrow {
    fill: none;
    stroke: var(--brand-blue);
    stroke-width: 3;
    stroke-linecap: round;
    stroke-linejoin: round;
  }
  .element-label {
    fill: var(--paper);
    stroke: var(--brand-blue);
    stroke-width: 1.1;
    font-size: 23px;
    letter-spacing: 0.5px;
    text-transform: uppercase;
  }
  .hub-arc-label {
    fill: var(--brand-blue);
    font-size: 24px;
  }
  .hub-name {
    fill: var(--brand-blue);
    font-size: 44px;
    font-weight: 400;
    letter-spacing: 1px;
  }
</style>
</head>
<body>
<svg class="framework" viewBox="0 0 1200 1000" xmlns="http://www.w3.org/2000/svg">
  <defs>
    <radialGradient id="icon-tone" cx="45%" cy="40%" r="65%">
      <stop offset="0%" stop-color="#eef4fb"/>
      <stop offset="60%" stop-color="#a9c3e2"/>
      <stop offset="100%" stop-color="#5d8cc4"/>
    </radialGradient>
    <path id="arc-brokerage" d="M415.5 303.4 A72 72 0 0 1 535.9 271.1"/>
    <path id="arc-integration" d="M686.3 272 A75 75 0 0 1 775.5 388.2"/>
    <path id="arc-trust" d="M785.8 648.9 A92 92 0 0 0 848.5 591.5"/>
    <path id="arc-incentives" d="M503.8 724 A88 88 0 0 0 656.2 724"/>
    <path id="arc-leadership" d="M303.4 506.2 A90 90 0 0 0 380.2 626.7"/>
    <path id="arc-community" d="M522 462 A68 68 0 0 1 656 466"/>
    <path id="arc-management" d="M512 510 A80 80 0 0 0 664 510"/>
  </defs>

  <circle class="orbit-ring" cx="588" cy="490" r="218"/>

  <g class="hub">
    <text class="hub-arc-label"><textPath href="#arc-community" startOffset="50%" text-anchor="middle">COMMUNITY</textPath></text>
    <text class="hub-name" x="588" y="506" text-anchor="middle">KORVEN</text>
    <text class="hub-arc-label"><textPath href="#arc-management" startOffset="50%" text-anchor="middle">Management</textPath></text>
  </g>

  <g class="element element-brokerage">
    <circle class="element-badge" cx="485" cy="322" r="62"/>
    <circle class="element-badge-inner" cx="485" cy="322" r="52"/>
    <circle class="element-icon" cx="485" cy="322" r="46" role="img" aria-label="Tin-can telephone icon"/>
    <text class="element-label"><textPath href="#arc-brokerage" startOffset="50%" text-anchor="middle">Brokerage</textPath></text>
  </g>

  <g class="element element-integration">
    <circle class="element-badge" cx="718" cy="340" r="64"/>
    <circle class="element-badge-inner" cx="718" cy="340" r="54"/>
    <circle class="element-icon" cx="718" cy="340" r="48" role="img" aria-label="Interlocking puzzle pieces icon"/>
    <text class="element-label"><textPath href="#arc-integration" startOffset="50%" text-anchor="middle">Integration</textPath></text>
  </g>

  <g class="element element-trust">
    <circle class="element-badge" cx="762" cy="560" r="62"/>
    <circle class="element-badge-inner" cx="762" cy="560" r="52"/>
    <circle class="element-icon" cx="762" cy="560" r="46" role="img" aria-label="Handshake icon"/>
    <text class="element-label"><textPath href="#arc-trust" startOffset="50%" text-anchor="middle">Trust</textPath></text>
  </g>

  <g class="element element-incentives">
    <circle class="element-badge" cx="580" cy="676" r="62"/>
    <circle class="element-badge-inner" cx="580" cy="676" r="52"/>
    <g class="growth-chart">
      <rect class="chart-bar" x="546" y="688" width="22" height="14" rx="3"/>
      <rect class="chart-bar" x="571" y="674" width="22" height="28" rx="3"/>
      <rect class="chart-bar" x="596" y="656" width="22" height="46" rx="3"/>
      <path class="chart-arrow" d="M548 672 L604 634"/>
      <path class="chart-arrow" d="M589 633 L604 634 L598 648"/>
    </g>
    <text class="element-label"><textPath href="#arc-incentives" startOffset="50%" text-anchor="middle">Incentives</textPath></text>
  </g>

  <g class="element element-leadership">
    <circle class="element-badge" cx="388" cy="537" r="62"/>
    <circle class="element-badge-inner" cx="388" cy="537" r="52"/>
    <circle class="element-icon" cx="388" cy="537" r="46" role="img" aria-label="Whistle icon"/>
    <text class="element-label"><textPath href="#arc-leadership" startOffset="50%" text-anchor="middle">Leadership</textPath></text>
  </g>
</svg>
</body>
</html>
```